Website Re-design and extension of an existing website

I have a Wordpress website currently and I need it to be upgraded. I have MOST of the content to get it started and the rest (video's, pictures ect) are on the way. I want to know if it is possible to convert my existing website into a Personal Brand website with a public speaking emphasis. I would like to have my website modeled after the following website:

http://www.kvaltomira.example/

I have attached a document entitled "Website Outline & Content" that has all of the text on it and it has red headlines that indicate where something needs to be added or designed. I will be happy to give more detail if needed.

Things I still need to get to you in order to design the website;

-Demo video
-Full length public speaking video

Target Market(s)

Corporations, universities, trade associations, private events

Coding

Coded - Design and coding required

Requirements
Must have
• Pictures, links, downloadable forms, MULTIPLE video's embedded, my logo, keep the colors in sync with my existing marketing material
Nice to have
• I would like my design colors thematic as already inherent in my marketing materials (see my Speaker One Sheet)

```html
<!DOCTYPE html>
<html lang="en">
<head>
<meta charset="utf-8">
<title>Dane Holloway – Holistic Lifestyle Hacker</title>
<link href="https://fonts.googleapis.com/css2?family=Oswald:wght@500;600;700&family=Open+Sans:ital,wght@0,400;0,600;0,700;1,400&display=swap" rel="stylesheet">
<style>
:root{
  --ink-dark:#2b3326;
  --nav-dark:#3a4433;
  --olive:#7f8f45;
  --olive-deep:#6f7e3a;
  --lime:#c9d44a;
  --accent-text:#7d9235;
  --text:#444;
  --muted:#777;
  --light:#f1f1ee;
  --white:#fff;
  --footer:#2f3330;
}
*{margin:0;padding:0;box-sizing:border-box}
html,body{width:1200px;height:2736px;overflow:hidden}
body{font-family:"Open Sans",Arial,sans-serif;color:var(--text);background:var(--white);font-size:15px}
section,header,footer{position:relative;width:1200px;overflow:hidden}

.topbar{height:88px;background:var(--ink-dark);display:flex;align-items:center;justify-content:space-between;padding:0 40px}
.brand{font-family:"Oswald",sans-serif;font-weight:700;font-size:32px;letter-spacing:1px;color:var(--lime);display:flex;align-items:center;gap:12px}
.brand-dot{width:28px;height:28px;border-radius:50%;background:var(--lime)}
.connect{display:flex;align-items:center;gap:14px;color:var(--white);font-size:13px;font-weight:600}
.social-dot{width:22px;height:22px;border-radius:50%;background:#5d6b4f}

.mainnav{height:40px;background:var(--nav-dark);display:flex;align-items:center;justify-content:center;gap:28px;font-size:13px;color:#e6e9dd}
.mainnav span:first-child{color:var(--lime)}

.hero{height:532px}
.hero-photo{position:absolute;inset:0;background:linear-gradient(180deg,#8fa3b8 0%,#a9b5bf 35%,#6c7560 60%,#4c4a3a 100%)}
.hero-box{position:absolute;left:560px;top:24px;width:610px;height:480px;background:rgba(30,36,28,.82);text-align:center;padding:30px 30px 0;color:var(--white)}
.hero-name{font-family:"Oswald",sans-serif;font-weight:700;font-size:46px;letter-spacing:2px}
.hero-roles{color:var(--lime);font-weight:600;font-size:16px;line-height:1.5;margin-top:10px}
.hero-tag{font-family:"Oswald",sans-serif;font-weight:500;font-size:34px;line-height:1.25;margin-top:22px}
.hero-btn{display:inline-block;background:var(--olive);color:var(--white);font-size:15px;font-weight:600;padding:14px 26px;margin-top:26px}
.hero-links{margin-top:28px;font-size:14px;font-weight:600;line-height:2;text-decoration:underline}

.stealth{height:260px;text-align:center;padding-top:60px}
.section-title{font-size:30px;font-weight:600;color:var(--accent-text)}
.stealth-list{list-style:none;display:grid;grid-template-columns:300px 300px;justify-content:center;gap:18px 80px;margin-top:34px;text-align:left;font-size:17px}
.stealth-list li{display:flex;align-items:center;gap:10px}
.stealth-list li::before{content:"";width:9px;height:9px;border-radius:50%;background:var(--olive)}

.promo{height:440px;background:var(--olive)}
.promo h2{position:absolute;left:40px;top:52px;color:var(--white);font-size:30px;font-weight:600}
.promo-text{position:absolute;left:40px;top:120px;width:540px;color:#eef1e2;font-size:14px;line-height:1.75}
.promo-video{position:absolute;left:620px;top:104px;width:460px;height:260px;background:linear-gradient(135deg,#d7d7d2,#9a9a95);box-shadow:0 0 0 6px rgba(255,255,255,.25)}
.play{position:absolute;left:200px;top:100px}

.split{height:400px;display:grid;grid-template-columns:1fr 1fr;gap:60px;padding:40px 40px 0}
.split h2{font-size:28px;font-weight:600;color:var(--accent-text);border-bottom:2px solid var(--olive);padding-bottom:10px;margin-bottom:20px}
.quote{font-size:13px;font-style:italic;line-height:1.6;color:var(--muted)}
.person{display:flex;align-items:center;gap:14px;margin:12px 0 22px}
.avatar{width:46px;height:46px;background:#b8a58e}
.person b{display:block;font-size:14px;color:var(--accent-text)}
.person small{font-size:12px;color:var(--muted)}
.article{display:flex;gap:18px;margin-bottom:22px}
.thumb{flex:0 0 150px;height:120px}
.article h3{font-size:16px;font-weight:700;color:var(--accent-text);line-height:1.35}
.article p{font-size:12.5px;line-height:1.55;color:var(--muted);margin-top:6px}
.article em{display:block;font-style:normal;font-size:12px;font-weight:700;color:var(--text);margin-top:6px}

.clients{height:200px;background:var(--light);text-align:center;padding-top:36px}
.clients h2{font-size:28px;font-weight:600;color:var(--text)}
.client-row{display:flex;justify-content:center;align-items:center;gap:40px;margin-top:38px;font-size:21px;font-weight:700;color:#3d3d3d}

.optin{height:460px;background:var(--olive-deep)}
.optin h2{position:absolute;left:40px;top:52px;width:780px;color:var(--white);font-size:30px;font-weight:600;line-height:1.3}
.form{position:absolute;left:40px;top:180px;width:600px}
.form-row{display:flex;gap:12px}
.field{flex:1;height:44px;background:var(--white);font-size:13px;color:#888;padding:12px}
.field.area{height:100px;margin-top:12px}
.submit{display:inline-block;margin-top:16px;background:var(--ink-dark);color:var(--white);font-weight:600;font-size:14px;padding:13px 26px}
.book{position:absolute;left:860px;top:70px;width:220px;height:330px;background:linear-gradient(160deg,#f4f4ef,#d9d6c9);box-shadow:8px 8px 0 rgba(0,0,0,.2)}

.site-footer{height:316px;background:var(--footer);color:#c8ccc0;display:grid;grid-template-columns:290px 390px 250px 190px;padding:48px 40px 0;font-size:13px}
.site-footer .brand{font-size:24px}
.site-footer .brand-dot{width:22px;height:22px}
.foot-note{margin-top:16px;line-height:1.7}
.site-footer h4{color:var(--white);font-size:15px;font-weight:600;margin-bottom:14px}
.cols{display:grid;grid-template-columns:210px 160px;gap:0 10px}
.site-footer ul{list-style:none;line-height:2.05}
.icon-line{display:flex;align-items:center;gap:10px}
.mini-dot{width:12px;height:12px;border-radius:50%;background:var(--olive)}
</style>
</head>
<body>

<header class="topbar">
  <div class="brand"><span class="brand-dot"></span>DANE HOLLOWAY</div>
  <div class="connect">Connect with Dane <span class="social-dot"></span><span class="social-dot"></span><span class="social-dot"></span><span class="social-dot"></span></div>
</header>

<nav class="mainnav">
  <span>Home</span><span>About Dane Holloway</span><span>Motivational Speaker Presenter</span><span>Workshop Presenter</span><span>Author</span><span>Coaching</span><span>Blog</span><span>Online Courses</span><span>Contact Dane Holloway</span>
</nav>

<section class="hero">
  <div class="hero-photo" role="img" aria-label="Photo of the speaker smiling outdoors with mountains and sky behind him"></div>
  <div class="hero-box">
    <div class="hero-name">DANE HOLLOWAY</div>
    <div class="hero-roles">Sugar Addiction Expert, Holistic Health Expert,<br>Author &amp; Speaker</div>
    <div class="hero-tag">Your Holistic Lifestyle Hacker<br>Lose Your Mind &amp; Find Your Health!</div>
    <div class="hero-btn">See How Dane Holloway Can Help You or Your Organization</div>
    <div class="hero-links">Download Dane's Speaker One Sheet | Download Dane's Media Sheet<br>Download Dane's College Speaker One Sheet</div>
  </div>
</section>

<section class="stealth">
  <h2 class="section-title">Sugar Addiction (The Stealth Addiction) is destroying:</h2>
  <ul class="stealth-list">
    <li>Your bottom line</li><li>Your Insurance Premiums</li>
    <li>The health of your employees</li><li>The culture of your company</li>
  </ul>
</section>

<section class="promo">
  <h2>Promo Video</h2>
  <p class="promo-text">For over 15 years, Dane Holloway has helped executives, employees and everyday people achieve lasting health and fitness by helping them "lose their minds." Using his unique 3-Quadrant Coaching System, speaking platform, and online training courses, Dane has helped hundreds of people reclaim their energy, break sugar habits and transform their bodies and minds. Dane delights in helping people see through the self-deception of eating "normal," and he invites his students to discover who they really are. If you are ready to feel better physically, mentally and emotionally, it is time to meet Dane.</p>
  <div class="promo-video" role="img" aria-label="Video still of the speaker talking to camera">
    <svg class="play" width="60" height="60" viewBox="0 0 60 60"><circle cx="30" cy="30" r="29" fill="#fff"/><path d="M24 18 L42 30 L24 42 Z" fill="#6f7e3a"/></svg>
  </div>
</section>

<section class="split">
  <div class="testimonials">
    <h2>Testimonials</h2>
    <p class="quote">" Vestibulum vel tellus ut amet turpis bibendum tincidunt vel sit amet quam. Pellentesque habitant morbi tristique senectus et netus et malesuada fames ac turpis egestas..."</p>
    <div class="person"><span class="avatar" role="img" aria-label="Portrait of a reviewer"></span><div><b>Name Heading</b><small>Location</small></div></div>
    <p class="quote">" Vestibulum vel tellus ut amet turpis bibendum tincidunt vel sit amet quam. Pellentesque habitant morbi tristique senectus et netus et malesuada fames ac turpis egestas..."</p>
    <div class="person"><span class="avatar" role="img" aria-label="Portrait of a reviewer"></span><div><b>Name Heading</b><small>Location</small></div></div>
  </div>
  <div class="press">
    <h2>Press Kit</h2>
    <div class="article"><span class="thumb" role="img" aria-label="Photo of a child eating junk food" style="background:linear-gradient(135deg,#d98a4c,#8a6a3c)"></span><div><h3>Why You Continue To Eat Junk Food Despite Your "Will Power"</h3><p>How Our Modern Eating Habits Made It Impossible To Say "No" To Junk Food? Hello, my friends...</p><em>Read More</em></div></div>
    <div class="article"><span class="thumb" role="img" aria-label="Photo of a woman stepping on a bathroom scale" style="background:linear-gradient(135deg,#c94b4b,#8a3030)"></span><div><h3>3 Reasons Why You Are Not Losing Weight Long Term...</h3><p>Hello my friends! How are you? I really hope that you had a great Thanksgiving! I was fortunate enough...</p><em>Read More</em></div></div>
  </div>
</section>

<section class="clients">
  <h2>Clients</h2>
  <div class="client-row"><span>Vitalis Weekly</span><span>Northfield</span><span>Courier Daily</span><span>Byteline</span><span>Newsround 7</span><span>Everyday Journal</span></div>
</section>

<section class="optin">
  <h2>Become a Holistic Health Hacker and receive a FREE 30-Day Meal Plan crafted by Dane!</h2>
  <div class="form">
    <div class="form-row"><div class="field">Name</div><div class="field">Email Address</div><div class="field">Phone No</div></div>
    <div class="field area">Message</div>
    <div class="submit">Get My Free E-Book</div>
  </div>
  <div class="book" role="img" aria-label="Cover of the speaker's book with title lettering and an illustration"></div>
</section>

<footer class="site-footer">
  <div>
    <div class="brand"><span class="brand-dot"></span>DANE HOLLOWAY</div>
    <p class="foot-note">Copyright 2017 Dane Holloway.<br>All Rights Reserved.</p>
  </div>
  <div>
    <h4>Site Map</h4>
    <div class="cols">
      <ul><li>Home</li><li>About Dane Holloway</li><li>Motivational Speaker Presenter</li><li>Workshop Presenter</li><li>Author</li></ul>
      <ul><li>Coaching</li><li>Blog</li><li>Online Courses</li><li>Contact Dane Holloway</li></ul>
    </div>
  </div>
  <div>
    <h4>Contact Info</h4>
    <ul>
      <li class="icon-line"><svg width="12" height="12" viewBox="0 0 12 12"><path d="M2 1h3l1 3-2 1a7 7 0 0 0 3 3l1-2 3 1v3c-6 0-10-4-10-9z" fill="#8c9c4a"/></svg>1-555-210-5470</li>
      <li class="icon-line"><svg width="12" height="12" viewBox="0 0 12 12"><rect x="1" y="3" width="10" height="7" fill="none" stroke="#8c9c4a"/><path d="M1 3l5 4 5-4" fill="none" stroke="#8c9c4a"/></svg>info@kvaltomira.example</li>
      <li class="icon-line"><span class="mini-dot"></span>Contact Form</li>
    </ul>
  </div>
  <div>
    <h4>Connect Me</h4>
    <ul>
      <li class="icon-line"><span class="mini-dot"></span>Friendwall</li>
      <li class="icon-line"><span class="mini-dot"></span>Chirpline</li>
      <li class="icon-line"><span class="mini-dot"></span>Workgraph</li>
      <li class="icon-line"><span class="mini-dot"></span>Clipstream</li>
    </ul>
  </div>
</footer>

</body>
</html>
```